Waterproofing Construction company needs letterhead

I need a letterhead design for a commercial waterproofing construction company. We would like to see designs that are contemporary, clean, sleek and use our logo. Our current design is dated. I would also like a cover page (see example) that goes with our letterhead. I would like for the footer to have our address, website, and phone number

Target Market(s)

Customers, potential customers.

Font styles to use
Sans Serif

Requirements
Must have
• logo, website, address, phone numbers, only our colors, tahoma font
• PMS: 295C PMS: 2995C
• CMYK: 100/84/36/39 CMYK: 80/12/1/0
• RGB: 16/44/82 RGB: 0/167/224
• HEX#: #102C52 HEX#: #00A7E0
• Black & White: 100% Black & White: 32%
• Gray Scale: 90% Gray Scale: 32%
Nice to have
• Our "icon" logo attached would be nice somewhere on the page.

```html
<!DOCTYPE html>
<html lang="en">
<head>
<meta charset="utf-8">
<title>KVR Waterproofing – Letterhead and Cover Page</title>
<link rel="stylesheet" href="https://fonts.googleapis.com/css2?family=Noto+Sans:wght@400;700;800&display=swap">
<style>
  :root {
    --navy: #0a1f5c;
    --sky: #3bb4e6;
    --paper: #ffffff;
    --ink: #111111;
    --backdrop: #ffffff;
  }
  * { margin: 0; padding: 0; box-sizing: border-box; }
  html, body {
    width: 1200px; height: 1000px; overflow: hidden;
    background: var(--backdrop);
    font-family: "Noto Sans", Tahoma, sans-serif;
  }
  .canvas { position: relative; width: 1200px; height: 1000px; }

  .sheet { position: absolute; width: 612px; height: 791px; }

  .cover {
    left: 529px; top: 52px;
    background: var(--navy);
  }
  .letterhead {
    left: 69px; top: 153px;
    background: var(--paper);
    border: 1px solid #d8d8d8;
  }

  .brand { position: absolute; }
  .brand-name {
    display: block;
    font-weight: 800;
    font-size: 50px;
    line-height: 44px;
    letter-spacing: -1px;
  }
  .brand-tagline {
    display: block;
    font-size: 8.6px;
    letter-spacing: 0.1px;
    margin-top: 4px;
  }
  .letterhead .brand { left: 31px; top: 23px; }
  .letterhead .brand-name { color: var(--navy); }
  .letterhead .brand-tagline { color: var(--sky); }

  .cover .brand { left: 220px; top: 365px; }
  .cover .brand-name { color: var(--paper); }
  .cover .brand-tagline { color: var(--paper); }

  .letter-body {
    position: absolute;
    left: 103px; top: 211px;
    width: 440px;
    color: var(--ink);
    font-size: 10.4px;
    line-height: 18.4px;
  }
  .letter-body p { margin-bottom: 3px; }
  .letter-body .salutation { margin-bottom: 6px; }

  .footer-band {
    position: absolute;
    left: 0; bottom: 0;
    width: 100%; height: 86px;
    background: var(--navy);
    color: var(--paper);
    font-size: 11px;
    padding: 15px 0 0 28px;
  }
  .contact-line {
    display: flex; align-items: center;
    height: 19px;
  }
  .contact-line svg { width: 11px; height: 11px; margin-right: 9px; flex: none; }
  .contact-line strong { font-weight: 700; }
</style>
</head>
<body>
<main class="canvas">

  <section class="sheet cover" aria-label="Cover page">
    <div class="brand">
      <span class="brand-name">KVR</span>
      <span class="brand-tagline">WATERPROOFING • RESTORATION</span>
    </div>
  </section>

  <section class="sheet letterhead" aria-label="Letterhead">
    <div class="brand">
      <span class="brand-name">KVR</span>
      <span class="brand-tagline">WATERPROOFING • RESTORATION</span>
    </div>

    <div class="letter-body">
      <p class="salutation">Lorem ipsum dolor sit amet,</p>
      <p>Consectetuer adipiscing elit, sed diam nonummy nibh euismod tincidunt ut laoreet<br>
      dolore magna aliquam erat volutpat. Ut wisi enim ad minim veniam, quis nostrud<br>
      exerci tation ullamcorper suscipit lobortis nisl ut aliquip ex ea commodo consequat.<br>
      Duis autem vel eum iriure dolor in hendrerit in vulputate velit esse molestie conse-<br>
      quat, vel illum dolore eu feugiat nulla facilisis at vero eros et accumsan et iusto odio<br>
      dignissim qui blandit praesent luptatum zzril delenit augue duis dolore te feugait nulla<br>
      facilisi.</p>
      <p>Lorem ipsum dolor sit amet, cons ectetuer adipiscing elit, sed diam nonummy nibh<br>
      euismod tincidunt ut laoreet dolore magna aliquam erat volutpat. Ut wisi enim ad<br>
      minim veniam, quis nostrud exerci tation ullamcorper suscipit lobortis nisl ut aliquip ex<br>
      ea commodo consequat.</p>
      <p>Lorem ipsum dolor sit amet, consectetuer adipiscing elit, sed diam nonummy nibh<br>
      euismod tincidunt ut laoreet dolore magna aliquam erat volutpat. Ut wisi enim ad<br>
      minim veniam, quis nostrud exerci tation ullamcorper suscipit lobortis nisl ut aliquip ex<br>
      ea commodo consequat. Duis autem vel eum iriure dolor in hendrerit in vulputate velit<br>
      esse molestie consequat, vel illum dolore eu feugiat nulla facilisis at vero eros et<br>
      accumsan et iusto odio dignissim qui blandit praesent luptatum zzril delenit augue duis<br>
      dolore te feugait nulla facilisi.</p>
    </div>

    <footer class="footer-band">
      <div class="contact-line">
        <svg viewBox="0 0 12 12" aria-hidden="true" fill="none" stroke="currentColor" stroke-width="1">
          <circle cx="6" cy="6" r="5"/><ellipse cx="6" cy="6" rx="2.2" ry="5"/><line x1="1" y1="6" x2="11" y2="6"/>
        </svg>
        <strong>www.KVRwp.com</strong>
      </div>
      <div class="contact-line">
        <svg viewBox="0 0 12 12" aria-hidden="true" fill="currentColor">
          <path d="M2.3 1 4.2 1 5 3.6 3.8 4.6C4.5 6 5.9 7.4 7.4 8.2L8.4 7 11 7.8 11 9.7C11 10.4 10.4 11 9.7 11 5 10.7 1.3 7 1 2.3 1 1.6 1.6 1 2.3 1Z"/>
        </svg>
        <span>PO Box 417 | Linden, NC 27610 | <strong>O:</strong> (877) 555-0142 | <strong>F:</strong> (919) 555-0187</span>
      </div>
      <div class="contact-line">
        <svg viewBox="0 0 12 12" aria-hidden="true" fill="currentColor">
          <path d="M6 0.5C3.8 0.5 2.2 2.1 2.2 4.2 2.2 7 6 11.5 6 11.5S9.8 7 9.8 4.2C9.8 2.1 8.2 0.5 6 0.5ZM6 5.6A1.4 1.4 0 1 1 6 2.8 1.4 1.4 0 0 1 6 5.6Z"/>
        </svg>
        <strong>North Carolina | South Carolina | Virginia</strong>
      </div>
    </footer>
  </section>

</main>
</body>
</html>
```